Conservative, Modern and Sharp Builder Business card

Hi there,
We would like to update our existing business card.
I have attached photos of existing business card, logo and van sign.

I would like the business card to also list what we do :
Renovation • New Build • Alteration
Extension • Bathroom • Maintenance.(Seperated by dots)

Contact number : 021 0483 0752
(With that exact spacing)

Ideally when people looking from about 2-3 metres, they know that it is a builder’s business card

Open to suggestions on fonts, layout, style of business card

PLEASE ONLY SUBMIT YOUR BEST OR MAX 3 DESIGNS FOR EACH DESIGNER

Thanks

Industry/Entity Type

Construction. Renovation

Contact Information for Business Card

Details should be the same as the existing card. And addition of what we do.

Requirements
Should not have
• The new business card must not have the same layout as our existing one. Thanks

```html
<!DOCTYPE html>
<html lang="en">
<head>
<meta charset="utf-8">
<title>KestrelBuild Business Card</title>
<link rel="stylesheet" href="https://fonts.googleapis.com/css2?family=Lato:wght@400;700;900&family=Roboto:wght@300;400&display=swap">
<style>
  :root {
    --stage: #9a9a9a;
    --paper: #ffffff;
    --paper-tone: #e6e6e7;
    --ink: #111111;
    --night: #111112;
    --night-tone: #202123;
    --on-night: #ffffff;
    --muted-ink: #333333;
  }
  * { box-sizing: border-box; margin: 0; padding: 0; }
  html, body { width: 1067px; height: 1200px; overflow: hidden; }
  body {
    background: var(--stage);
    display: flex;
    flex-direction: column;
    align-items: center;
    justify-content: center;
    gap: 76px;
  }
  .card {
    position: relative;
    width: 860px;
    height: 491px;
    overflow: hidden;
  }

  /* Front */
  .card--front {
    background: linear-gradient(120deg, var(--paper) 0%, var(--paper) 45%, var(--paper-tone) 100%);
    color: var(--ink);
  }
  .front-wordmark {
    position: absolute;
    left: 48px; top: 226px;
    width: 330px;
    text-align: center;
    font: 900 46px/1 "Lato", sans-serif;
    color: var(--ink);
    letter-spacing: -0.5px;
  }
  .divider {
    position: absolute;
    left: 429px; top: 132px;
    width: 2px; height: 238px;
    background: var(--ink);
  }
  .person { position: absolute; left: 449px; top: 126px; }
  .person-name { font: 700 47px/1 "Lato", sans-serif; letter-spacing: -0.3px; }
  .person-role { font: 400 27px/1 "Lato", sans-serif; margin-top: 4px; color: var(--muted-ink); }
  .contact { position: absolute; left: 449px; font: 300 23px/1 "Roboto", sans-serif; color: var(--muted-ink); display: flex; align-items: center; gap: 12px; }
  .contact svg { width: 16px; height: 16px; fill: var(--ink); }
  .contact--phone { top: 239px; }
  .contact--email { top: 276px; }
  .contact-icons { position: absolute; left: 449px; top: 318px; display: flex; gap: 10px; }
  .contact-icons svg { width: 16px; height: 16px; }
  .contact--web { top: 346px; }

  /* Back */
  .card--back {
    background: linear-gradient(120deg, var(--night) 0%, var(--night) 40%, var(--night-tone) 100%);
    color: var(--on-night);
  }
  .back-mark {
    position: absolute;
    left: 408px; top: 96px;
    width: 44px; height: 44px;
    background: var(--on-night);
  }
  .back-wordmark {
    position: absolute;
    left: 0; right: 0; top: 196px;
    text-align: center;
    font: 700 72px/1 "Lato", sans-serif;
    letter-spacing: -0.5px;
  }
  .services-label {
    position: absolute;
    left: 0; right: 0; top: 331px;
    display: flex; justify-content: center; align-items: center; gap: 12px;
    font: 700 24px/1 "Lato", sans-serif;
    letter-spacing: 1.5px;
  }
  .services-label::before, .services-label::after {
    content: ""; width: 116px; height: 1.5px; background: var(--on-night);
  }
  .services-list {
    position: absolute;
    left: 0; right: 0; top: 373px;
    text-align: center;
    font: 400 23.5px/1.18 "Lato", sans-serif;
  }
</style>
</head>
<body>

<section class="card card--front" aria-label="Business card front">
  <div class="front-wordmark">KestrelBuild</div>
  <div class="divider"></div>
  <div class="person">
    <div class="person-name">Marten Holloway</div>
    <div class="person-role">Residential Builder</div>
  </div>
  <div class="contact contact--phone">
    <svg viewBox="0 0 24 24" aria-hidden="true"><path d="M6.6 2.5l3 3.3-1.8 2.4c1.2 3 3.9 5.8 7 7l2.4-1.8 3.3 3-1.8 3.4C11.6 20 4 12.4 3.2 4.3z"/></svg>
    <span>021 0483 0752</span>
  </div>
  <div class="contact contact--email">
    <svg viewBox="0 0 24 24" aria-hidden="true"><path d="M2 5h20v14H2z" fill="var(--ink)"/><path d="M3.5 7l8.5 6 8.5-6" fill="none" stroke="var(--paper)" stroke-width="1.6"/></svg>
    <span>KestrelBuild@mailbox.co.nz</span>
  </div>
  <div class="contact-icons" aria-hidden="true">
    <svg viewBox="0 0 24 24"><circle cx="12" cy="12" r="10" fill="none" stroke="var(--ink)" stroke-width="2"/><path d="M2 12h20M12 2c-4 5-4 15 0 20M12 2c4 5 4 15 0 20" fill="none" stroke="var(--ink)" stroke-width="1.6"/></svg>
    <svg viewBox="0 0 24 24"><rect x="2" y="2" width="20" height="20" fill="var(--ink)"/></svg>
  </div>
  <div class="contact contact--web"><span>KestrelBuild.nz</span></div>
</section>

<section class="card card--back" aria-label="Business card back">
  <div class="back-mark" aria-hidden="true"></div>
  <div class="back-wordmark">KestrelBuild</div>
  <div class="services-label">SERVICES</div>
  <div class="services-list">
    Renovation • New Build • Alteration<br>
    Extension • Bathroom • Maintenance
  </div>
</section>

</body>
</html>
```